Business Card for a Creative Technology based HR services company

Our company name is Leaf8, and we build large communities of HR (human resource) and finance personnels through our mobile platform, and we conduct lots of on-line and off-line activities to get everyone constantly connected. Behind all these, we will also provide on-site HR and finance contractors to our clients, plus a host of other HR-related services. No process in our company takes more than 5-steps.
Our company slogan: Shaping Your Tomorrow
Target Market(s)
All human resource (HR) and finance personnels, from new entrants to highly experienced senior professionals.
Industry/Entity Type
Finance
Colors
Designer to choose colors to be used in the design.
Look and feel
Each slider illustrates characteristics of the customer's brand and the style your logo design should communicate.

```html
<!DOCTYPE html>
<html lang="en">
<head>
<meta charset="utf-8">
<title>Leaf8 Business Card</title>
<link rel="stylesheet" href="https://fonts.googleapis.com/css2?family=Marcellus&family=Marcellus+SC&display=swap">
<style>
  :root {
    --navy: #10305e;
    --navy-deep: #0c2750;
    --red: #e0262a;
    --paper: #f4f4f4;
    --ink: #3a3d42;
    --stage: #e6e4e0;
    --white: #ffffff;
  }
  * { margin: 0; padding: 0; box-sizing: border-box; }
  html, body { width: 1200px; height: 900px; overflow: hidden; }
  body {
    background: var(--stage);
    font-family: "Marcellus", Georgia, serif;
    position: relative;
  }
  .card {
    position: absolute;
    left: 260px;
    width: 680px;
    height: 389px;
    box-shadow: 0 6px 18px rgba(0,0,0,0.18);
    overflow: hidden;
  }

  /* Back of card */
  .card-back { top: 45px; background: var(--navy-deep); }
  .card-back .brand {
    position: absolute;
    top: 118px;
    left: 0; right: 0;
    display: flex;
    justify-content: center;
    align-items: center;
    gap: 12px;
    color: var(--white);
    font-size: 44px;
    letter-spacing: 1px;
  }
  .brand-dot {
    width: 18px; height: 18px;
    border-radius: 50%;
    background: var(--red);
  }
  .card-back .web {
    position: absolute;
    top: 178px; left: 0; right: 0;
    text-align: center;
    color: var(--white);
    font-size: 9px;
    letter-spacing: 2px;
  }
  .slogan-band {
    position: absolute;
    top: 200px; left: 0; right: 0;
    height: 24px;
    background: var(--red);
    display: flex;
    align-items: center;
    justify-content: center;
  }
  .slogan {
    font-family: "Marcellus SC", Georgia, serif;
    color: var(--white);
    font-size: 12px;
    letter-spacing: 3px;
  }

  /* Front of card */
  .card-front { top: 466px; background: var(--paper); }
  .card-front .brand {
    position: absolute;
    top: 92px; left: 56px;
    display: flex;
    align-items: center;
    gap: 12px;
    color: var(--navy);
    font-size: 58px;
    letter-spacing: 1px;
  }
  .card-front .brand-dot { width: 24px; height: 24px; }
  .person { position: absolute; top: 110px; left: 366px; }
  .person-name {
    font-family: "Marcellus SC", Georgia, serif;
    color: var(--ink);
    font-size: 20px;
    letter-spacing: 4px;
  }
  .person-title {
    color: var(--navy);
    font-size: 12px;
    letter-spacing: 2px;
    margin-top: 2px;
  }
  .address {
    position: absolute;
    top: 172px; left: 366px;
    color: var(--ink);
    font-size: 12px;
    letter-spacing: 1.5px;
    line-height: 18px;
  }
  .contacts {
    position: absolute;
    top: 226px; left: 332px;
    list-style: none;
  }
  .contacts li {
    display: flex;
    align-items: center;
    gap: 14px;
    height: 20px;
    color: var(--ink);
    font-size: 12px;
    letter-spacing: 1.5px;
  }
  .contacts svg { width: 14px; height: 14px; flex: none; }
  .icon-stroke { fill: none; stroke: var(--red); stroke-width: 1.6; stroke-linecap: round; stroke-linejoin: round; }
</style>
</head>
<body>

<section class="card card-back" aria-label="Card back">
  <div class="brand"><span class="brand-name">Leaf8</span><span class="brand-dot"></span></div>
  <div class="web">www.leaf8.com</div>
  <div class="slogan-band"><span class="slogan">Shaping Your Tomorrow</span></div>
</section>

<section class="card card-front" aria-label="Card front">
  <div class="brand"><span class="brand-name">Leaf8</span><span class="brand-dot"></span></div>

  <div class="person">
    <div class="person-name">Dana Morrow</div>
    <div class="person-title">CEO</div>
  </div>

  <div class="address">
    2710 Alder Row, Suite #4<br>
    Fairbrook, CA 95012
  </div>

  <ul class="contacts">
    <li>
      <svg viewBox="0 0 16 16" aria-hidden="true"><path class="icon-stroke" d="M4 2h2l1 3-1.5 1a8 8 0 0 0 4.5 4.5L11 9l3 1v2a2 2 0 0 1-2 2A10 10 0 0 1 2 4a2 2 0 0 1 2-2z"/></svg>
      555-210-4817
    </li>
    <li>
      <svg viewBox="0 0 16 16" aria-hidden="true"><rect class="icon-stroke" x="2" y="6" width="12" height="7" rx="1"/><path class="icon-stroke" d="M5 6V2h6v4M5 10h6"/></svg>
      555-210-4900
    </li>
    <li>
      <svg viewBox="0 0 16 16" aria-hidden="true"><rect class="icon-stroke" x="4.5" y="1.5" width="7" height="13" rx="1.5"/><path class="icon-stroke" d="M7 12h2"/></svg>
      555-362-0193
    </li>
    <li>
      <svg viewBox="0 0 16 16" aria-hidden="true"><rect class="icon-stroke" x="1.5" y="3.5" width="13" height="9" rx="1"/><path class="icon-stroke" d="M2 4l6 5 6-5"/></svg>
      dmorrow@leaf8.com
    </li>
    <li>
      <svg viewBox="0 0 16 16" aria-hidden="true"><circle class="icon-stroke" cx="8" cy="8" r="6.5"/><path class="icon-stroke" d="M1.5 8h13M8 1.5c2.5 2 2.5 11 0 13M8 1.5c-2.5 2-2.5 11 0 13"/></svg>
      www.leaf8.com
    </li>
  </ul>
</section>

</body>
</html>
```